Mobile version of Desktop site

I need a mobile version of my desktop site. Up until now we have been using a mobile translation service but there are too many drawbacks and bugs. So I need a mobile site designed to be used on an Zephyr or android phone that is "Inspired by" our desktop site. I am going to setup two completely separate sites, served either as desktop or mobile.

I have attached an eps version of my logo.

Design this site as though the largest screen it will be viewed on is an Zephyr 4 max, but more likely it will be viewed on smaller screens.

Phone number as a button to click to call should be prominent.

Just need a basic attorney website that is clean and has the look and feel of the desktop site, but readable and usable on a smartphone.

Base your design off of an inner page like whats on this url:
Desktop url: https://www.brambleworthlegal.com/corvana-heights.html
Updates

Reason: I am extending the deadline to allow for implementation of feedback

Target Market(s)

everyone

Industry/Entity Type

Attorney

Number of Pages Required

1 page

Font styles to use
Sans Serif

Requirements
Must have
• Must be readable and usable on a smart phone, from a 5.5" Zephyr 4 max on down to the original Zephyr. I'm looking for usability and readability.
Nice to have
• I would like to see logos shown at the top filling the width of the page if viewed in portrait mode with the phone number next, and it should be a complementing version of my desktop site.
Should not have
• I do not want to see a lot of small details that would be lost on a smartphone platform.

```html
<!DOCTYPE html>
<html lang="en">
<head>
<meta charset="utf-8">
<title>Brambleworth Attorneys – Mobile</title>
<link href="https://fonts.googleapis.com/css2?family=Open+Sans:wght@400;600&display=swap" rel="stylesheet">
<style>
  :root {
    --navy: #1a3f6f;
    --text: #3f3f3f;
    --muted: #7a7a7a;
    --accent: #b0282a;
    --panel: #ebebeb;
    --field-border: #d4d4d4;
    --white: #ffffff;
    --social-1: #3b5998;
    --social-2: #4da7de;
    --social-3: #2b78b5;
    --social-4: #333333;
    --social-5: #c9302c;
  }
  * { box-sizing: border-box; margin: 0; padding: 0; }
  html, body { width: 799px; height: 1200px; overflow: hidden; background: var(--white); }
  body { font-family: "Open Sans", Arial, sans-serif; color: var(--text); position: relative; }

  .site-header { position: absolute; top: 0; left: 0; width: 799px; height: 140px; }
  .brand-name {
    position: absolute; left: 17px; top: 46px; width: 640px;
    font-size: 46px; font-weight: 600; color: var(--navy);
    letter-spacing: 0.5px; line-height: 56px; white-space: nowrap;
  }
  .menu-button {
    position: absolute; left: 701px; top: 41px; width: 81px; height: 81px;
    background: var(--navy); border-radius: 7px; border: none;
  }
  .menu-button span {
    position: absolute; left: 20px; width: 41px; height: 6px;
    background: var(--white); border-radius: 2px;
  }
  .menu-button span:nth-child(1) { top: 26px; }
  .menu-button span:nth-child(2) { top: 38px; }
  .menu-button span:nth-child(3) { top: 50px; }

  .call-block { position: absolute; top: 190px; left: 0; width: 799px; text-align: center; }
  .call-label { font-size: 37px; line-height: 56px; color: var(--text); }
  .call-label em { font-style: normal; color: var(--accent); }
  .call-number {
    display: block; font-size: 68px; font-weight: 600; line-height: 84px;
    color: var(--text); text-decoration: none; letter-spacing: 1px;
  }

  .social-row { position: absolute; top: 381px; left: 0; width: 799px; display: flex; justify-content: center; gap: 20px; }
  .social-dot { width: 64px; height: 64px; border-radius: 50%; display: block; }
  .social-dot.s1 { background: var(--social-1); }
  .social-dot.s2 { background: var(--social-2); }
  .social-dot.s3 { background: var(--social-3); }
  .social-dot.s4 { background: var(--social-4); }
  .social-dot.s5 { background: var(--social-5); }

  .hero-photo {
    position: absolute; top: 508px; left: 0; width: 799px; height: 255px;
    background: linear-gradient(180deg, #3f86cf 0%, #7fb4e2 32%, #2a6fb5 48%, #1d5fa6 62%, #7c8a8a 80%, #3e5f85 100%);
  }

  .contact-panel {
    position: absolute; top: 829px; left: 52px; width: 701px; height: 400px;
    background: var(--panel);
  }
  .panel-tab {
    position: absolute; top: 865px; left: 33px; width: 506px; height: 77px;
    background: var(--navy); color: var(--white);
    font-size: 42px; line-height: 77px; padding-left: 42px; white-space: nowrap;
  }
  .panel-tab-fold { position: absolute; top: 942px; left: 33px; }
  .panel-subtitle {
    position: absolute; top: 950px; left: 86px;
    font-size: 30px; line-height: 42px; color: var(--text);
  }
  .form-field {
    position: absolute; left: 84px; width: 637px; height: 89px;
    background: var(--white); border: 2px solid var(--field-border); border-radius: 5px;
    font-family: inherit; font-size: 25px; color: var(--muted);
    padding: 0 34px; line-height: 85px;
  }
  .field-name { top: 1024px; }
  .field-email { top: 1141px; }
</style>
</head>
<body>
  <header class="site-header">
    <div class="brand-name">Brambleworth Attorneys</div>
    <button class="menu-button" aria-label="Menu"><span></span><span></span><span></span></button>
  </header>

  <section class="call-block">
    <p class="call-label">Call Now For <em>Free</em> Consultation</p>
    <a class="call-number" href="tel:5553184720">(555) 318-4720</a>
  </section>

  <nav class="social-row" aria-label="Social links">
    <span class="social-dot s1"></span>
    <span class="social-dot s2"></span>
    <span class="social-dot s3"></span>
    <span class="social-dot s4"></span>
    <span class="social-dot s5"></span>
  </nav>

  <div class="hero-photo" role="img" aria-label="Aerial panorama of a coastal harbor with sandy peninsula, blue bay and city under a blue sky"></div>

  <section class="contact-form">
    <div class="contact-panel"></div>
    <div class="panel-tab">How Can We Help You?</div>
    <svg class="panel-tab-fold" width="19" height="20" viewBox="0 0 19 20"><polygon points="0,0 19,0 19,20" fill="#0f2a4d"/></svg>
    <p class="panel-subtitle">Talk To Us About Your Injury Now</p>
    <div class="form-field field-name">Name</div>
    <div class="form-field field-email">E-mail</div>
  </section>
</body>
</html>
```